Template design for organic gardening site for ShopVantra platform

We need a template design for our new 'Fen Leaf Naturals' shopvantra site. Fen Leaf Naturals specialises in organic nutrients for gardening plus all equipment needed to grow.
Domain name will be www.fenleafnaturals.co.uk
Colours used should include logo colours, see attached image. Other colours to compliment the greens and lift the feel of the site could be yellow or orange.
Home page design should include, but not limited to the following:
Interactive banner carousel space
A smaller banner advertising space
Featured products
New products
Sale products feature/link
Articles links/feature
+ all standard shopvantra features such as menus, etc
The site will be selling products (these are nutrients) such as:
Pelvarimost
Marsh hare soil tonic
Terrawix
Nuro pods
Stem triumph
Sprout charm
Vel
Flint amber
Moswelder
+ more products and brands
Site layouts we like include:
www.tidemarkaquafarm.co.uk ... A bit old fashioned but cool
www.lanternbeds.co.uk ... Nice but too compact
www.flintamber.com ... Has a nice top half
www.sponsorapod.org.uk ... Nice colours and header
www.penhurstplants.co.uk ... nice layout, but needs image carousel
www.wrenmeal.co.uk ... Nice background and colours
www.thistle.co.uk ... Nice colours and layout
www.danielmorrowhorticulture.com ... Nice layout and header
www.sprivant.co.uk ... Cool colours and shop pages layout is nice
www.aquavenor.co.uk ... One of the best layouts
The site should feel clean, modern and elegant.
Target Market(s)
Indoor and outdoor organic gardeners
Look and feel

```html
<!DOCTYPE html>
<html lang="en">
<head>
<meta charset="utf-8">
<title>Fen Leaf Naturals — Home</title>
<link rel="stylesheet" href="https://fonts.googleapis.com/css2?family=Roboto:wght@300;400;500;700&display=swap">
<style>
:root{
  --sky-top:#3f8fd8;
  --sky-low:#b3d8f2;
  --grass:#3d6a1c;
  --forest:#1b3312;
  --forest-deep:#0f1e0b;
  --footer:#2c4024;
  --footer-base:#121c0f;
  --leaf:#5cb82e;
  --leaf-dark:#3c7a1f;
  --link:#6fcf3a;
  --offer:#9a7410;
  --banner:#d3e3f4;
  --text:#ffffff;
  --muted:#c9d6c2;
  --nav:#3d4d5e;
}
*{box-sizing:border-box;margin:0;padding:0}
html,body{width:910px;height:1200px;overflow:hidden}
body{position:relative;font-family:'Roboto',sans-serif;color:var(--text);background:var(--forest-deep)}
a{color:inherit;text-decoration:none}
.scenery{position:absolute;left:0;top:23px;width:910px;height:871px;
  background:linear-gradient(180deg,var(--sky-top) 0%,#7fb9e8 12%,var(--sky-low) 22%,#8fbf63 25%,var(--grass) 28%,var(--forest) 38%,#14270e 70%,var(--forest-deep) 100%)}
.topbar{position:absolute;left:0;top:0;width:910px;height:23px;background:#fff;font-size:7.5px;color:#555}
.topbar .phone{position:absolute;left:464px;top:8px;font-weight:500}
.topbar .currency{position:absolute;left:588px;top:8px}
.topbar .basket{position:absolute;left:672px;top:6px}
.brand{position:absolute;left:224px;top:44px;display:flex;align-items:center;gap:7px}
.brand .mark{width:30px;height:30px;background:var(--leaf-dark);border-radius:5px}
.brand .name{font-size:17px;font-weight:700;color:var(--leaf-dark);line-height:1}
.search{position:absolute;left:555px;top:58px;width:130px;height:20px;background:#fff;border:1px solid #c8d8e6;font-size:7px;font-style:italic;color:#666;padding:6px 7px}
.search svg{position:absolute;right:6px;top:4px}
.main-nav{position:absolute;left:224px;top:96px;width:462px;height:19px;border-bottom:1px solid rgba(255,255,255,.6);font-size:7.5px;color:var(--nav)}
.main-nav a{position:absolute;top:0}
.hero{position:absolute;left:224px;top:129px;width:462px;height:213px;background:#fff}
.hero .slide{position:absolute;left:9px;top:9px;width:443px;height:194px;background:var(--banner)}
.dots{position:absolute;left:437px;top:348px;display:flex;gap:6px}
.dots span{width:8px;height:8px;border-radius:50%;background:#fff}
.dots .on{background:var(--leaf);border:1.5px solid #fff}
.section-title{position:absolute;left:224px;top:382px;font-size:13.5px;font-weight:300}
.product-row{position:absolute;left:224px;width:462px;height:216px;
  background:linear-gradient(180deg,rgba(0,0,0,.22),rgba(0,0,0,0));display:flex;gap:12px;padding:10px 9px}
.product{position:relative;width:102px;font-size:7.5px;line-height:11px}
.product .photo{position:relative;width:102px;height:102px;background:#fff;overflow:hidden}
.product .photo svg{position:absolute;right:0;top:0}
.product .title{margin-top:14px;height:22px}
.product .offer{display:inline-block;background:var(--offer);padding:0 6px;height:10px;line-height:10px;margin-top:-11px;margin-left:1px}
.product .price{font-weight:700;color:var(--muted);margin-top:1px}
.product .add{display:inline-block;margin-top:5px;background:var(--leaf);font-weight:700;font-size:7px;padding:5px 10px;border-radius:1px}
.site-footer{position:absolute;left:0;top:894px;width:910px;height:240px;background:var(--footer)}
.col{position:absolute;top:32px;width:102px;font-size:7.3px}
.col h3{font-size:10px;font-weight:300;padding-bottom:8px;border-bottom:1px solid rgba(255,255,255,.12);margin-bottom:8px}
.col li{list-style:none;color:var(--link);height:14.7px}
.news dt{font-size:6px;text-transform:uppercase;margin-top:5px}
.news dd{color:var(--link);line-height:10px;margin-top:2px;margin-bottom:8px}
.newsletter p{margin-bottom:12px}
.newsletter .field{height:14px;background:#5f7157;margin-bottom:9px}
.newsletter .signup{display:inline-block;background:var(--leaf-dark);font-weight:700;font-size:7px;padding:5px 10px}
.newsletter h4{font-size:10px;font-weight:300;margin-top:20px}
.social{display:flex;gap:7px;margin-top:7px}
.social span{width:11px;height:11px;background:var(--leaf-dark)}
.base{position:absolute;left:0;top:1134px;width:910px;height:66px;background:var(--footer-base)}
.base nav{position:absolute;left:234px;top:14px;font-size:7.5px;font-weight:500}
.base nav a{position:absolute;top:0;white-space:nowrap}
.base .legal{position:absolute;left:234px;top:30px;font-size:5.5px;color:#8a9684}
</style>
</head>
<body>
<div class="scenery" role="img" aria-label="Blue sky with clouds and hanging leaves above a green grass horizon"></div>

<header class="topbar">
  <span class="phone">Telephone us on 01632 960 418</span>
  <span class="currency">All prices are in &nbsp;£GBP</span>
  <svg class="basket" width="11" height="9" viewBox="0 0 11 9"><path d="M1 3h9l-1.5 5h-6z" fill="#999"/><path d="M3 3l2-2.5M8 3L6 .5" stroke="#999" fill="none"/></svg>
</header>

<a class="brand" href="#"><span class="mark"></span><span class="name">Fen Leaf<br>Naturals</span></a>

<div class="search">Search
  <svg width="10" height="11" viewBox="0 0 10 11"><circle cx="6" cy="4" r="3" fill="none" stroke="#6a8fb0" stroke-width="1.2"/><path d="M4 6L1 10" stroke="#6a8fb0" stroke-width="1.4"/></svg>
</div>

<nav class="main-nav">
  <a style="left:0" href="#">Home</a><a style="left:42px" href="#">About Us</a><a style="left:96px" href="#">Our Products</a><a style="left:162px" href="#">Sale</a><a style="left:200px" href="#">FAQs</a><a style="left:240px" href="#">Contact Us</a>
</nav>

<section class="hero"><div class="slide" role="img" aria-label="Carousel banner slide"></div></section>
<div class="dots"><span class="on"></span><span></span><span></span></div>

<h2 class="section-title">Featured Products</h2>

<div class="product-row" style="top:408px">
  <article class="product"><div class="photo" role="img" aria-label="Product photo"></div><p class="title">Product name to go on this space here</p><p class="price">£20.00</p><a class="add" href="#">Add to basket</a></article>
  <article class="product"><div class="photo" role="img" aria-label="Product photo"></div><p class="title">Product name to go on this space here</p><p class="price">£20.00</p><a class="add" href="#">Add to basket</a></article>
  <article class="product"><div class="photo" role="img" aria-label="Product photo"><svg width="40" height="40" viewBox="0 0 40 40"><path d="M0 0h14l26 26v14z" fill="var(--leaf)"/><text x="23" y="15" transform="rotate(45 23 15)" font-size="6.5" fill="#fff" text-anchor="middle" font-family="Roboto,sans-serif">SALE</text></svg></div><p class="title">Product name to go on this space here</p><p class="price">£20.00</p><a class="add" href="#">Add to basket</a></article>
  <article class="product"><div class="photo" role="img" aria-label="Product photo"></div><p class="title">Product name to go on this space here</p><p class="price">£20.00</p><a class="add" href="#">Add to basket</a></article>
</div>

<div class="product-row" style="top:657px">
  <article class="product"><div class="photo" role="img" aria-label="Product photo"></div><p class="title">Product name to go on this space here</p><p class="price">£20.00</p><a class="add" href="#">Add to basket</a></article>
  <article class="product"><div class="photo" role="img" aria-label="Product photo"><svg width="40" height="40" viewBox="0 0 40 40"><path d="M0 0h14l26 26v14z" fill="var(--leaf)"/><text x="23" y="15" transform="rotate(45 23 15)" font-size="6.5" fill="#fff" text-anchor="middle" font-family="Roboto,sans-serif">SALE</text></svg></div><p class="title">Product name to in here<br><span class="offer">Introductory Offer</span></p><p class="price">£20.00</p><a class="add" href="#">Add to basket</a></article>
  <article class="product"><div class="photo" role="img" aria-label="Product photo"><svg width="40" height="40" viewBox="0 0 40 40"><path d="M0 0h14l26 26v14z" fill="var(--leaf)"/><text x="23" y="15" transform="rotate(45 23 15)" font-size="6.5" fill="#fff" text-anchor="middle" font-family="Roboto,sans-serif">SALE</text></svg></div><p class="title">Product name to go&nbsp; here<br><span class="offer">Introductory Offer</span></p><p class="price">£20.00</p><a class="add" href="#">Add to basket</a></article>
  <article class="product"><div class="photo" role="img" aria-label="Product photo"></div><p class="title">Product name to go on this space here</p><p class="price">£20.00</p><a class="add" href="#">Add to basket</a></article>
</div>

<footer class="site-footer">
  <div class="col" style="left:234px"><h3>Popular Brands</h3><ul>
    <li>Pelvarimost</li><li>Marsh hare soil tonic</li><li>Terrawix</li><li>Nuro pods</li><li>Stem triumph</li><li>Sprout charm</li><li>Vel</li><li>Flint amber</li><li>Moswelder</li></ul></div>
  <div class="col" style="left:347px"><h3>Categories</h3><ul>
    <li>Complete Grow Kits</li><li>Plant Lighting</li><li>Environment Control</li><li>Grow Tents</li><li>Grow Systems</li><li>Grow Mediums</li><li>Pots and Trays</li><li>Nutrients and Additives</li><li>Nutrient Control</li><li>Pumps &amp; Tank Heaters</li></ul></div>
  <div class="col news" style="left:460px"><h3>Recent Updates</h3><dl>
    <dt>New product</dt><dd>Product title in this space</dd>
    <dt>News story</dt><dd>News article title to be placed in this space here</dd>
    <dt>New product</dt><dd>Product title in this space</dd>
    <dt>New product</dt><dd>Product title in here</dd></dl></div>
  <div class="col newsletter" style="left:574px"><h3>Newsletter</h3>
    <p>Sign up for our newsletter here</p>
    <div class="field"></div><div class="field"></div>
    <a class="signup" href="#">Sign Up</a>
    <h4>Connect with us</h4>
    <div class="social"><span></span><span></span><span></span></div>
  </div>
</footer>

<div class="base">
  <nav><a style="left:0" href="#">Home</a><a style="left:42px" href="#">About Us</a><a style="left:95px" href="#">Our Products</a><a style="left:162px" href="#">Sale</a><a style="left:200px" href="#">FAQs</a><a style="left:240px" href="#">Contact Us</a></nav>
  <p class="legal">© 2015 Fen Leaf Naturals . All rights reserved</p>
</div>
</body>
</html>
```